Velmora Diagnostics Website

Project Description – Velmora Website Design
We need a clean, modern, and professional website for Velmora Diagnostics, a Ashgrove Hollis University of Dunmere spin-out focused on early cancer detection. Our first product, GlandSURE™, is a urine-based risk assessment test for pancreatic cancer, supported by strong clinical validation and partnerships with leading hospitals.

The site should:

Communicate trust, innovation, and clinical credibility.
Feature a clear value proposition on the home page with strong calls to action for investors, clinicians, and partners.
Showcase our technology, science, and clinical evidence in a way that is accessible but authoritative.
Highlight our university heritage, team, and collaborators.
Include sections for products/services, news/press, and contact forms.
Be fully responsive, WordPress compatible, SEO-friendly, and WCAG 2.1 AA accessible.

We want a minimalist, elegant design with subtle animations, strong visuals (e.g., science/biotech imagery), and a clear structure for future growth.
Deliverables should include editable design files (Figma/Sketch/Adobe XD) and a style guide.

```html
<!DOCTYPE html>
<html lang="en">
<head>
<meta charset="utf-8">
<title>Velmora Diagnostics</title>
<link href="https://fonts.googleapis.com/css2?family=Barlow:wght@400;500;600&family=Inter+Tight:wght@600;700&display=swap" rel="stylesheet">
<style>
:root{
  --navy:#1b1a73;
  --navy-deep:#15145e;
  --ink:#17166b;
  --yellow:#f5c23a;
  --card:#eaeef3;
  --muted:#5b5f73;
  --white:#fff;
}
*{margin:0;padding:0;box-sizing:border-box}
html,body{width:1200px;height:2731px;overflow:hidden}
body{position:relative;font-family:"Barlow",sans-serif;color:var(--ink);background:linear-gradient(#fff 1700px,#eef1f8 2358px)}
.abs{position:absolute}
.head{font-family:"Inter Tight",sans-serif;font-weight:700;letter-spacing:-.03em}
.accent{color:var(--yellow)}
.eyebrow{font-size:12.5px;font-weight:600;letter-spacing:.24em;text-transform:uppercase}

.hero{left:0;top:0;width:1200px;height:748px;background:radial-gradient(circle at 70% 45%,#3b2c98 0,#23217c 45%,#1c1a6b 100%);color:var(--white)}
.logo{display:flex;align-items:center;gap:10px;font-family:"Barlow",sans-serif;font-weight:600;font-size:22px;letter-spacing:.08em;color:#4fa3e8}
.logo-dot{width:22px;height:22px;border-radius:50%;background:var(--yellow)}
.nav{left:408px;top:58px;display:flex;gap:28px;font-size:13px;font-weight:600;letter-spacing:.06em}
.nav .on{color:var(--yellow)}
.btn{left:860px;top:47px;width:166px;height:38px;border-radius:20px;background:var(--yellow);color:var(--navy);font-size:13px;font-weight:600;letter-spacing:.06em;display:flex;align-items:center;justify-content:center}
.cell{left:660px;top:150px;width:500px;height:500px;border-radius:50%;background:radial-gradient(circle at 50% 48%,#c24bd0 0,#8f36b8 20%,#5a3aa6 38%,#4a3c9f 62%,rgba(60,50,150,.4) 75%,transparent 76%)}
.hero h1{left:170px;top:262px;font-size:62px;line-height:63px}
.hero p{left:170px;top:457px;width:540px;font-size:15.5px;line-height:24px}
.learn{left:170px;top:519px;height:54px;border-left:2px solid var(--white);padding-left:16px;font-size:13px;font-weight:600;letter-spacing:.1em}
.learn::before{content:"";position:absolute;left:-2px;top:0;width:2px;height:18px;background:var(--yellow)}

.edge h2{font-size:44px;line-height:47px}
.card{width:270px;height:265px;border-radius:14px;background:var(--card);padding:26px 22px}
.card h3{font-family:"Inter Tight",sans-serif;font-weight:700;font-size:22px;letter-spacing:-.03em;line-height:24px;height:66px}
.card p{font-size:13px;line-height:19.5px;color:var(--muted)}
.card.dark{background:linear-gradient(160deg,#27249a,#1c1a75);color:var(--white)}
.card.dark h3{height:90px}
.card.dark p{color:#d6d8f0}
.ico{position:absolute;right:22px;bottom:22px;width:46px;height:46px;border-radius:6px;background:var(--white);display:flex;align-items:center;justify-content:center}
.dark .ico{background:var(--yellow)}
.molecule{left:35px;top:1220px;width:130px;height:120px;border-radius:50%;background:radial-gradient(circle,#c9dcf5,rgba(255,255,255,0))}
.video{left:170px;top:1266px;width:855px;height:496px;border-radius:30px;background:linear-gradient(120deg,#2b3f78,#3e5a9c 45%,#a9bfe0 75%,#4a6aa8)}
.play{left:552px;top:1468px;width:92px;height:92px;border-radius:50%;border:3px solid var(--white);display:flex;align-items:center;justify-content:center}

.impact h2{left:0;width:1200px;text-align:center;font-size:37px;line-height:40.5px}
.stat{width:270px;border-radius:14px;background:var(--white);text-align:center;box-shadow:0 8px 30px rgba(30,40,100,.06)}
.stat b{display:block;font-family:"Inter Tight",sans-serif;font-weight:700;font-size:66px;letter-spacing:-.04em;line-height:66px}
.stat .eyebrow{font-size:12px;letter-spacing:.28em}
.stat p{font-size:13px;line-height:19.5px;color:var(--muted);padding:0 20px}

.footer{left:0;top:2358px;width:1200px;height:373px;background:linear-gradient(180deg,#1b1a78,#17166a);color:var(--white)}
.footer h4{font-family:"Inter Tight",sans-serif;font-weight:700;font-size:18px;letter-spacing:-.02em}
.footer ul{list-style:none;font-size:13.5px;line-height:25.5px;margin-top:12px}
.footer .txt{font-size:13.5px;line-height:19.5px}
.contact li{display:flex;gap:8px;margin-bottom:20px;line-height:19.5px}
.social{width:42px;height:42px;border-radius:50%;border:1.5px solid rgba(255,255,255,.8)}
.legal{display:flex;gap:12px;font-size:13px}
</style>
</head>
<body>

<header class="hero abs">
  <div class="cell abs" role="img" aria-label="Glowing purple cancer cell floating in blue fluid"></div>
  <div class="logo abs" style="left:170px;top:50px"><span class="logo-dot"></span>Velmora DX</div>
  <nav class="nav abs"><span class="on">HOME</span><span>ABOUT US</span><span>OUR PRODUCT</span><span>BLOG</span><span>CONTACT US</span></nav>
  <div class="btn abs">PARTNER WITH US</div>
  <div class="eyebrow abs" style="left:170px;top:242px">Combining biomarker panels with <span class="accent">advanced analytics</span></div>
  <h1 class="head abs">For Surveillance<br>And <span class="accent">Early Detection</span><br>Of Cancer</h1>
  <p class="abs">Non-invasive, urine-based diagnostics utilize urine to detect and monitor various diseases without needing invasive procedures.</p>
  <div class="learn abs">LEARN MORE</div>
</header>

<section class="edge">
  <div class="eyebrow abs" style="left:170px;top:805px">Our edge in early detection</div>
  <h2 class="head abs" style="left:170px;top:825px">The Future of <span class="accent">Pancreatic Cancer</span> Surveillance<br>Where Leading Science Meets Care.</h2>
  <div class="card abs" style="left:170px;top:940px"><h3>Non-invasive, Painless</h3><p>We believe the greatest breakthroughs happen when you embrace uncertainty and refuse to give up.</p><div class="ico"><svg width="22" height="22"><path d="M4 19L18 5" stroke="#1b1a73" stroke-width="3" stroke-linecap="round"/><circle cx="15" cy="16" r="3" fill="#1b1a73"/></svg></div></div>
  <div class="card abs" style="left:463px;top:940px"><h3>Precision Biomarkers</h3><p>We believe the greatest breakthroughs happen when you embrace uncertainty and refuse to give up.</p><div class="ico"><svg width="22" height="24"><path d="M5 2C5 10 17 14 17 22M17 2C17 10 5 14 5 22" stroke="#1b1a73" stroke-width="3" fill="none"/></svg></div></div>
  <div class="card dark abs" style="left:755px;top:940px"><h3>Clinically validated &amp; University Spin-out Heritage</h3><p>We believe the greatest breakthroughs happen when you embrace uncertainty and refuse to give up.</p><div class="ico"><svg width="22" height="24"><path d="M8 2h6v7l6 12H2L8 9z" fill="#1b1a73"/></svg></div></div>
  <div class="card abs" style="left:1048px;top:940px"><h3>AI-powered Insights</h3><p>We believe the greatest breakthroughs happen when you embrace uncertainty and refuse to give up.</p></div>
  <div class="molecule abs" role="img" aria-label="Glass molecule model decoration"></div>
  <div class="video abs" role="img" aria-label="Scientists in lab coats reviewing data on a monitor in a laboratory"></div>
  <div class="play abs"><svg width="16" height="18"><path d="M2 1l13 8-13 8z" fill="#fff"/></svg></div>
</section>

<section class="impact">
  <div class="eyebrow abs" style="left:0;width:1200px;text-align:center;top:1819px">Breakthrough science, real-world impact</div>
  <h2 class="head abs" style="top:1839px">Early Detection Is Critical To Improve<br><span class="accent">Pancreatic Cancer Outcomes</span>. So, Many<br>Scientists Focus Their Pancreatic Cancer<br>Research On Early Detection.</h2>
  <div class="stat abs" style="left:170px;top:2047px;height:250px;padding-top:42px"><b>86%</b><div class="eyebrow" style="margin:6px 0 54px">Sensitivity</div><p>We believe the greatest breakthroughs happen when you embrace uncertainty and refuse to give up.</p></div>
  <div class="stat abs" style="left:463px;top:2024px;height:251px;padding-top:42px"><b>&gt;1,000</b><div class="eyebrow" style="margin:6px 0 54px">Samples validated.</div><p>We believe the greatest breakthroughs happen when you embrace uncertainty and refuse to give up.</p></div>
  <div class="stat abs" style="left:755px;top:2047px;height:250px;padding-top:42px"><b>90%</b><div class="eyebrow" style="margin:6px 0 54px">Specificity</div><p>We believe the greatest breakthroughs happen when you embrace uncertainty and refuse to give up.</p></div>
</section>

<footer class="footer abs">
  <div class="logo abs" style="left:170px;top:68px;font-size:19px"><span class="logo-dot" style="width:20px;height:20px"></span>Velmora DX</div>
  <div class="abs" style="left:172px;top:128px;font-size:15px;line-height:17px;font-weight:500;width:200px">Ashgrove Hollis University of Dunmere</div>
  <p class="txt abs" style="left:170px;top:175px;width:200px">Spin-out focused on early cancer detection.</p>
  <div class="abs" style="left:411px;top:58px"><h4>Quick Links</h4><ul><li>Home</li><li>About Us</li><li>Our Product</li><li>Science</li><li>Contact Us</li></ul></div>
  <div class="abs" style="left:553px;top:58px;width:180px"><h4>Mission Statement</h4><p class="txt" style="margin-top:16px">We believe the greatest breakthroughs happen when you embrace uncertainty and refuse to give up.</p></div>
  <div class="abs contact" style="left:784px;top:58px;width:250px"><h4>Contact Us</h4>
    <ul class="txt" style="margin-top:16px">
      <li><svg width="12" height="14"><path d="M6 13S1 8 1 5a5 5 0 0110 0c0 3-5 8-5 8z" fill="#f5c23a"/><circle cx="6" cy="5" r="2" fill="#1b1a78"/></svg><span>Office: 48 Larkspur Lane Dunmere, DM4 7QT</span></li>
      <li><svg width="12" height="14"><path d="M2 1l3 0 1 3-2 1c1 2 2 3 4 4l1-2 3 1v3C7 11 2 6 2 1z" fill="#f5c23a"/></svg><span>Phone: (555) 014-2386</span></li>
      <li><svg width="12" height="14"><rect x="0" y="3" width="12" height="8" fill="#f5c23a"/><path d="M0 3l6 5 6-5" stroke="#1b1a78" fill="none"/></svg><span>Email: hello@velmoradiagnostics.com</span></li>
    </ul></div>
  <div class="txt abs" style="left:170px;top:282px">Copyright - © 2025 Velmora Diagnostics</div>
  <div class="social abs" style="left:536px;top:270px" aria-label="Social profile"></div>
  <div class="social abs" style="left:588px;top:270px" aria-label="Social profile"></div>
  <div class="social abs" style="left:640px;top:270px" aria-label="Social profile"></div>
  <div class="legal abs" style="left:771px;top:282px"><span>Terms of Service</span><span>Privacy Policy</span><span>Diclaimer</span></div>
</footer>

</body>
</html>
```